Newsletter Ad

I am looking for someone to design an advertisement for a mother's club newsletter. 4" wide X by 5" tall (and 2.5" wide X 5" tall if possible).

I'm a psychotherapist, so want the ad to look professional, but modern. I have a logo with my photo attached that can be incorporated into the design. The colors of my website are turquoise and white. I'd like to keep with that theme...so maybe some turquoise blocking to match the logo font color.

I'm uploading a logo as well as an ad draft with the content I'd like listed in the ad.

```html
<!DOCTYPE html>
<html lang="en">
<head>
<meta charset="utf-8">
<title>Dana Merritt – Psychotherapy Ad</title>
<link rel="stylesheet" href="https://fonts.googleapis.com/css2?family=Lato:wght@300;400&display=swap">
<style>
  :root {
    --teal: #1a9d9b;
    --teal-glow: #1fa9a9;
    --magenta: #b0005f;
    --white: #ffffff;
    --ring-light: #f7f7f7;
    --ring-shade: #d9dcdc;
    --portrait-dark: #1b1412;
    --portrait-warm: #8a6a52;
  }
  * { margin: 0; padding: 0; box-sizing: border-box; }
  html, body { width: 960px; height: 1200px; overflow: hidden; background: var(--teal); }
  .ad {
    position: relative;
    width: 960px;
    height: 1200px;
    background: radial-gradient(ellipse 60% 35% at 50% 18%, var(--teal-glow), var(--teal) 70%);
    font-family: "Lato", "Helvetica Neue", Arial, sans-serif;
    color: var(--white);
    text-align: center;
    overflow: hidden;
  }
  .portrait-frame {
    position: absolute;
    left: 303px;
    top: 32px;
    width: 354px;
    height: 354px;
    border-radius: 50%;
    background: linear-gradient(160deg, var(--ring-light), var(--ring-shade));
    box-shadow: 0 18px 30px rgba(0, 60, 60, 0.35);
  }
  .portrait {
    position: absolute;
    left: 32px;
    top: 32px;
    width: 290px;
    height: 290px;
    border-radius: 50%;
    background: radial-gradient(circle at 50% 55%, var(--portrait-warm) 0%, #5a4234 40%, var(--portrait-dark) 75%);
    box-shadow: inset 0 3px 8px rgba(0, 0, 0, 0.35);
  }
  .headline {
    position: absolute;
    top: 452px;
    left: 0;
    width: 100%;
    font-weight: 300;
    font-size: 70px;
    line-height: 68px;
    letter-spacing: 1px;
    text-transform: uppercase;
  }
  .services {
    position: absolute;
    top: 756px;
    left: 0;
    width: 100%;
    list-style: none;
    font-weight: 300;
    font-size: 27px;
    line-height: 27px;
  }
  .contact-band {
    position: absolute;
    left: 0;
    top: 1026px;
    width: 100%;
    height: 174px;
    background: var(--magenta);
    padding-top: 10px;
  }
  .practitioner {
    font-weight: 400;
    font-size: 55px;
    line-height: 62px;
  }
  .contact-line {
    font-weight: 300;
    font-size: 28px;
    line-height: 30px;
  }
</style>
</head>
<body>
  <main class="ad">
    <div class="portrait-frame">
      <div class="portrait" role="img" aria-label="Portrait photograph of the therapist"></div>
    </div>

    <h1 class="headline">Psychotherapy<br>for Individuals,<br>Couples<br>and Families</h1>

    <ul class="services">
      <li>Parenting</li>
      <li>Depression</li>
      <li>Anxiety</li>
      <li>Life Transitions</li>
      <li>Divorce</li>
      <li>Couples Issues</li>
      <li>Women’s Issues</li>
      <li>Attachment and Neuroscience</li>
    </ul>

    <footer class="contact-band">
      <p class="practitioner">DANA MERRITT,MA,MFT</p>
      <p class="contact-line">418 Harbor Lane, Cedar Cove, CA 94900</p>
      <p class="contact-line">www.danamerritt.com/ dana@danamerritt.com</p>
      <p class="contact-line">555.014.2290</p>
    </footer>
  </main>
</body>
</html>
```